Business Card Design

I already have a company logo for my company. I have a logo for the manufacturer we represent. I want a professional business card design.

```html
<!DOCTYPE html>
<html lang="en">
<head>
<meta charset="utf-8">
<title>Harbor Signal Group – Business Card</title>
<link href="https://fonts.googleapis.com/css2?family=Lato:wght@400;700&family=Montserrat:wght@700;800&display=swap" rel="stylesheet">
<style>
  :root {
    --page-bg: #2a2b2e;
    --card-bg: #1f1f22;
    --red: #e3202a;
    --gold: #e6ad24;
    --white: #ffffff;
    --text-soft: #d9d9dc;
    --divider: #4a4a4f;
  }
  * { box-sizing: border-box; margin: 0; padding: 0; }
  html, body { width: 1200px; height: 952px; overflow: hidden; }
  body {
    background: var(--page-bg);
    font-family: "Lato", Arial, sans-serif;
    position: relative;
  }
  .card {
    position: absolute;
    top: 327px;
    width: 525px;
    height: 300px;
    background: var(--card-bg);
    overflow: hidden;
    box-shadow: 0 14px 30px rgba(0,0,0,.45);
  }
  .card--front { left: 45px; }
  .card--back { left: 630px; }

  .accent-bar {
    position: absolute;
    width: 13px;
    height: 112px;
    background: var(--red);
  }
  .accent-bar--top { left: 0; top: 20px; }
  .accent-bar--bottom { right: 0; bottom: 20px; }

  .brand {
    display: flex;
    align-items: center;
    gap: 10px;
    font-family: "Montserrat", Arial, sans-serif;
    font-weight: 800;
    color: var(--white);
    letter-spacing: .5px;
    line-height: 1.1;
  }
  .brand-mark { background: var(--red); flex: none; }

  .card--front .brand {
    position: absolute;
    left: 46px;
    top: 96px;
    width: 200px;
    font-size: 17px;
  }
  .card--front .brand-mark { width: 20px; height: 20px; }

  .divider {
    position: absolute;
    left: 266px;
    top: 60px;
  }

  .address {
    position: absolute;
    left: 46px;
    bottom: 38px;
    font-size: 11.5px;
    color: var(--text-soft);
  }

  .person {
    position: absolute;
    left: 292px;
    top: 74px;
    width: 205px;
  }
  .person-name {
    font-family: "Montserrat", Arial, sans-serif;
    font-weight: 700;
    font-size: 15px;
    letter-spacing: .3px;
    color: var(--gold);
    white-space: nowrap;
  }
  .person-name .surname { color: var(--red); }
  .person-title {
    font-size: 12px;
    color: var(--text-soft);
    margin-top: 4px;
  }
  .contact-list {
    list-style: none;
    margin-top: 18px;
  }
  .contact-list li {
    display: flex;
    align-items: center;
    gap: 8px;
    font-size: 12px;
    color: var(--text-soft);
    margin-bottom: 7px;
  }
  .contact-list svg { width: 12px; height: 12px; flex: none; }

  .card--back .brand {
    position: absolute;
    left: 50%;
    top: 50%;
    transform: translate(-50%, -50%);
    font-size: 28px;
    white-space: nowrap;
  }
  .card--back .brand-mark { width: 28px; height: 28px; }
</style>
</head>
<body>

  <section class="card card--front">
    <span class="accent-bar accent-bar--top"></span>
    <span class="accent-bar accent-bar--bottom"></span>

    <div class="brand">
      <span class="brand-mark"></span>
      <span>HARBOR SIGNAL<br>GROUP</span>
    </div>

    <svg class="divider" width="2" height="150" viewBox="0 0 2 150">
      <line x1="1" y1="0" x2="1" y2="150" stroke="var(--divider)" stroke-width="1"/>
    </svg>

    <p class="address">2170 Lakeside Avenue Portland, OR 97205</p>

    <div class="person">
      <h1 class="person-name">DANIEL R. <span class="surname">WHITMORE</span></h1>
      <p class="person-title">Managing Director</p>
      <ul class="contact-list">
        <li>
          <svg viewBox="0 0 24 24"><path fill="var(--red)" d="M6.6 10.8a15.1 15.1 0 0 0 6.6 6.6l2.2-2.2c.3-.3.7-.4 1-.2 1.1.4 2.300.6 3.6.6.6 0 1 .4 1 1V20c0 .6-.4 1-1 1A17 17 0 0 1 3 4c0-.6.4-1 1-1h3.5c.6 0 1 .4 1 1 0 1.3.2 2.5.6 3.6.1.3 0 .7-.2 1z"/></svg>
          +00 987 654 32
        </li>
        <li>
          <svg viewBox="0 0 24 24"><path fill="var(--red)" d="M2 5h20v14H2z"/><path fill="none" stroke="var(--card-bg)" stroke-width="2" d="M2 5l10 8 10-8"/></svg>
          hello@harborsignal.com
        </li>
        <li>
          <svg viewBox="0 0 24 24"><circle cx="12" cy="12" r="9.5" fill="none" stroke="var(--red)" stroke-width="2.5"/><path fill="none" stroke="var(--red)" stroke-width="2" d="M2.5 12h19M12 2.5c3 3 3 16 0 19M12 2.5c-3 3-3 16 0 19"/></svg>
          www.harborsignal.com
        </li>
      </ul>
    </div>
  </section>

  <section class="card card--back">
    <div class="brand">
      <span class="brand-mark"></span>
      <span>HARBOR SIGNAL GROUP</span>
    </div>
  </section>

</body>
</html>
```